Marvel Brookworks highend custom homes

We build high end custom homes and timber frames we specialize in rustic hand made designs along with iron and concrete accents to add a modern touch 90% of my homes are buit on lake front properries attached is my logo and slogan as of now and my previous one

Target Market(s)

High end custom homes

Industry/Entity Type

Custom residential construction

Contact Information for Business Card

Been in buissness 8+ years inssured and reliable

Colors
A7469A
B969AE
D3A5CF
EDDBEB
F8F0F9

Requirements
Must have
• Must have slogan and phone number
Should not have
• A combination of rustic yet modern accents

```html
<!DOCTYPE html>
<html lang="en">
<head>
<meta charset="utf-8">
<title>Marvel Brookworks – Business Card</title>
<link rel="stylesheet" href="https://fonts.googleapis.com/css2?family=Jost:wght@300;400;600&display=swap">
<style>
  :root {
    --bg: #d8d8d8;
    --forest: #4b5c48;
    --forest-faint: #566a53;
    --paper: #ffffff;
    --ink-light: #f1f3ef;
    --shadow: rgba(0, 0, 0, 0.22);
  }
  * { box-sizing: border-box; margin: 0; padding: 0; }
  html, body {
    width: 1200px; height: 1200px; overflow: hidden;
    background: var(--bg);
    font-family: "Jost", "Helvetica Neue", Arial, sans-serif;
  }
  .canvas { position: relative; width: 1200px; height: 1200px; }

  .card {
    position: absolute; left: 184px; width: 831px; height: 487px;
    box-shadow: 0 3px 8px var(--shadow);
    overflow: hidden;
  }
  .card--front { top: 81px; background: var(--forest); }
  .card--back { top: 631px; display: flex; }

  /* Front: faint tonal name */
  .front-brand {
    position: absolute; inset: 0;
    display: flex; flex-direction: column; align-items: center; justify-content: center;
    color: var(--forest-faint);
  }
  .front-brand__name {
    font-weight: 600; font-size: 52px; letter-spacing: 1px; text-transform: uppercase;
    line-height: 1;
  }

  /* Back: brand panel */
  .brand-panel {
    width: 421px; height: 100%; background: var(--paper);
    display: flex; flex-direction: column; align-items: center; justify-content: center;
    color: var(--forest);
  }
  .brand-lockup { display: flex; align-items: center; gap: 16px; }
  .brand-lockup__square { width: 62px; height: 62px; background: var(--forest); }
  .brand-lockup__name {
    font-weight: 600; font-size: 38px; line-height: 1.02; text-transform: uppercase;
    letter-spacing: 0.5px;
  }
  .tagline {
    margin-top: 20px; font-weight: 400; font-size: 17px; letter-spacing: 0.6px;
    text-transform: uppercase;
  }

  /* Back: contact panel */
  .contact-panel {
    flex: 1; background: var(--forest); color: var(--ink-light);
    position: relative; font-weight: 300; font-size: 22px;
  }
  .contact-list { position: absolute; right: 50px; list-style: none; }
  .contact-list--reach { top: 137px; }
  .contact-list--post { top: 288px; }
  .contact-list li {
    display: flex; align-items: center; justify-content: flex-end; gap: 16px;
    height: 32px; letter-spacing: 0.2px; white-space: nowrap;
  }
  .icon { width: 14px; height: 14px; fill: none; stroke: var(--ink-light); stroke-width: 1.6; }
  .icon--solid { fill: var(--ink-light); stroke: none; }
  .icon-spacer { width: 14px; }
</style>
</head>
<body>
<main class="canvas">

  <section class="card card--front" aria-label="Card front">
    <div class="front-brand">
      <div class="front-brand__name">Marvel Brookworks</div>
    </div>
  </section>

  <section class="card card--back" aria-label="Card back">
    <div class="brand-panel">
      <div class="brand-lockup">
        <span class="brand-lockup__square"></span>
        <span class="brand-lockup__name">Marvel<br>Brookworks</span>
      </div>
      <div class="tagline">Lakeside homes built by hand</div>
    </div>

    <div class="contact-panel">
      <ul class="contact-list contact-list--reach">
        <li>+61 400 123 456
          <svg class="icon" viewBox="0 0 16 16" aria-hidden="true"><path d="M4 2l2.5 3-1.5 1.5c.8 2 2.5 3.7 4.5 4.5L11 9.5l3 2.5-1.5 2c-5 0-10.5-5.5-10.5-10.5z"/></svg>
        </li>
        <li>info@marvelbrookworks.com
          <svg class="icon" viewBox="0 0 16 16" aria-hidden="true"><rect x="1.5" y="3.5" width="13" height="9" class="icon--solid"/><path d="M2 4l6 5 6-5" stroke="#4b5c48"/></svg>
        </li>
        <li>www.marvelbrookworks.com
          <svg class="icon" viewBox="0 0 16 16" aria-hidden="true"><circle cx="8" cy="8" r="6.2"/><path d="M1.8 8h12.4M8 1.8c-3 3.5-3 8.9 0 12.4M8 1.8c3 3.5 3 8.9 0 12.4"/></svg>
        </li>
      </ul>
      <ul class="contact-list contact-list--post">
        <li>PO Box 210
          <svg class="icon" viewBox="0 0 16 16" aria-hidden="true"><path d="M8 14s-4.5-4.6-4.5-8a4.5 4.5 0 0 1 9 0c0 3.4-4.5 8-4.5 8z"/><circle cx="8" cy="6" r="1.6"/></svg>
        </li>
        <li>Kelpie Cove SA 0000<span class="icon-spacer"></span></li>
      </ul>
    </div>
  </section>

</main>
</body>
</html>
```